Lighter Decals - Sticker Designs - BrightWick

I am looking to have decal designs made that I can wrap the body of a plastic lighter with. I have included the lighter design template with the specific size of decal needed, including cut-out. The lighter is 3.25" tall and 1" wide and will be wrapped in a decal the size of the template.

These are separate and distinct lighters, but come from the same company, so a similar "feel" isn't a bad thing. Please submit separate designs, it's easier to give feedback that way.

1. The first lighter is called an "Copper Harbor" Flame and is targeted at tourists visiting Seattle. Please note that the Quill Tower is a trademarked image, even stylized representations of it cannot be used. I am open to creativity, but simple is best, while eye-catching. It can say Seattle on the opposite side from Copper Harbor, that's fine. But don't let me limit you. Regardless, it is intended to catch the eye and be somewhat of an impulse buy in tourist shops. But I won't sell eye-sores. The lighter trigger is a translucent green and glows in the dark. Some are black, with black bodies.

2. The second lighter is called a "731Kite" and is as you might have suspected, targeted at the cannabis crowd, both smoke shops and end users. The lighter trigger is a translucent green and glows in the dark for these as well. Lighter body is black, but that can be changed to match your design if warranted. I want 731Kite to be very legible. See below for the "brand band" I'm looking for incorporating my logo on each lighter. What to put on the back side of this lighter (the decal is a full wrap) is up to you, but I want pot smokers to enjoy using the lighter. Pot leaves, whatever, but with most things, I do like a simple, clean, smooth look. Polished you might say.

For both lighters, my company name is "BrightWick" with no space. I would like my logo (included file) and company name incorporated into the design of both lighters. Please choose a font for the company name that "suits" the logo (I call him Otto). Otto can be any color, doesn't have to be white, that's just the typical / default and it looks good on a number of background colors.

3. Based on the above, please note that I'd like a "default" BrightWick lighter decal made as well. Same product as the above, but not a 731 or Copper Harbor. This can be similar to the other two, but the only wording on there will be the company name. That and Otto, the logo. I want to focus on the first two lighters and then create the 3rd one once the others are finalized.

Please let me know if you have any questions.

Target Market(s)

1. tourists visiting Seattle, so the lighters will be sold to retail shops

2. any marijuana user, dispensary, smoke shop, etc.

Industry/Entity Type

Plastic

Requirements
Must have
• 1. Copper Harbor very legible
- targeted to Seattle tourists

2. 731Kite very legible
- targeted to pot consumers

3. The color green in each lighter design

4. A font for "BrightWick" that is usable on website, product, apparel, stickers, etc.
- the font should "suit" Otto and have the same company feel, fun and joyful
Nice to have
• A full wrap design, not segmented
Attractive image, fun to carry around
Should not have
• Emphasis specifically on the Quill Tower

```html
<!DOCTYPE html>
<html lang="en">
<head>
<meta charset="utf-8">
<title>731Kite Lighter Wrap – BrightWick</title>
<link rel="stylesheet" href="https://fonts.googleapis.com/css2?family=Kalam:wght@700&family=Kaushan+Script&display=swap">
<style>
  :root {
    --ink: #0f1210;
    --smoke-bright: #5dff2a;
    --smoke-mid: #2fd60f;
    --smoke-deep: #0f6a08;
    --type: #ffffff;
    --glow: rgba(255, 255, 255, 0.75);
  }
  * { margin: 0; padding: 0; box-sizing: border-box; }
  html, body { width: 1112px; height: 1200px; overflow: hidden; background: var(--ink); }
  .wrap-decal {
    position: relative;
    width: 1112px;
    height: 1200px;
    overflow: hidden;
    background: var(--ink);
  }
  .smoke-backdrop {
    position: absolute;
    inset: 0;
    background:
      radial-gradient(ellipse 60% 35% at 50% 100%, var(--smoke-bright) 0%, var(--smoke-mid) 35%, transparent 75%),
      radial-gradient(ellipse 30% 45% at 78% 40%, rgba(47, 214, 15, 0.7) 0%, transparent 70%),
      radial-gradient(ellipse 35% 30% at 18% 22%, rgba(47, 214, 15, 0.45) 0%, transparent 70%),
      radial-gradient(ellipse 40% 30% at 55% 8%, rgba(15, 106, 8, 0.6) 0%, transparent 70%),
      radial-gradient(ellipse 30% 40% at 10% 70%, rgba(47, 214, 15, 0.55) 0%, transparent 70%),
      var(--ink);
  }
  .brand-ring {
    position: absolute;
    border: 9px solid var(--type);
    border-radius: 50%;
  }
  .brand-ring--main { left: 172px; top: 307px; width: 224px; height: 224px; }
  .brand-ring--corner { left: 793px; top: 912px; width: 164px; height: 164px; }
  .brand-name {
    position: absolute;
    font-family: "Kaushan Script", cursive;
    color: var(--type);
    white-space: nowrap;
    transform: translate(-50%, -50%);
  }
  .brand-name--main { left: 284px; top: 419px; font-size: 38px; }
  .brand-name--corner { left: 875px; top: 1114px; font-size: 48px; }
  .product-number {
    position: absolute;
    left: 230px;
    top: 770px;
    font-family: "Kalam", cursive;
    font-weight: 700;
    font-size: 220px;
    line-height: 1;
    color: var(--type);
    text-shadow: 0 0 14px var(--glow), 0 0 4px var(--glow);
    transform: translate(-50%, -50%) rotate(-72deg);
    white-space: nowrap;
  }
  .product-word {
    position: absolute;
    left: 450px;
    top: 600px;
    font-family: "Kaushan Script", cursive;
    font-size: 96px;
    line-height: 1;
    color: var(--type);
    text-shadow: 0 0 12px var(--glow);
    transform: translate(-50%, -50%) rotate(-72deg);
    white-space: nowrap;
  }
</style>
</head>
<body>
  <main class="wrap-decal">
    <div class="smoke-backdrop" role="img" aria-label="Billowing green smoke swirling over a black background"></div>

    <div class="brand-ring brand-ring--main" aria-hidden="true"></div>
    <span class="brand-name brand-name--main">BrightWick</span>

    <span class="product-number">731</span>
    <span class="product-word">Kite</span>

    <div class="brand-ring brand-ring--corner" aria-hidden="true"></div>
    <span class="brand-name brand-name--corner">BrightWick</span>
  </main>
</body>
</html>
```